Riverpeak Analytics needs new design business card

We are video surveillance and analytics software development company.
I am looking for a professional business card.
Our website is www.riverpeakanalytics.example.au
Please have a loo and get the feel for who we are and what we do.
I do not know what else to give you apart from good luck and I hope your design gets selected.
Thank you very much for participating
Business
Contact Information for Business Card
Address
27/15 Marlowe Street Fernbrook NSW 2199
Telephone 1300 582 417
Mobile 0450 731 258
email: marcus@riverpeakanalytics.example.au
name
Marcus Helvard
Position
Managing Director
Font styles to use
Other font styles liked:
- Arial
Look and feel

```html
<!DOCTYPE html>
<html lang="en">
<head>
<meta charset="utf-8">
<title>Riverpeak Analytics – Business Card</title>
<link rel="stylesheet" href="https://fonts.googleapis.com/css2?family=Source+Sans+3:wght@400;600;700&display=swap">
<style>
  :root {
    --navy: #173c69;
    --slate: #6f7f8c;
    --mist: #c5ccd5;
    --white: #ffffff;
    --backdrop: #e8e5e0;
    --ink-soft: #5d6b78;
  }
  * { box-sizing: border-box; margin: 0; padding: 0; }
  html, body {
    width: 1200px; height: 1172px; overflow: hidden;
    background: var(--backdrop);
    font-family: "Source Sans 3", Arial, sans-serif;
  }
  .canvas { position: relative; width: 1200px; height: 1172px; }

  .card {
    position: absolute; width: 906px; height: 516px;
    border-radius: 30px; overflow: hidden;
    box-shadow: 0 4px 14px rgba(0,0,0,0.18);
  }

  /* Front */
  .card-front { left: 250px; top: 57px; background: var(--white); border: 1px solid #9aa3ad; }
  .brand {
    position: absolute; left: 54px; top: 92px;
    display: flex; align-items: center; gap: 18px;
  }
  .brand-mark { width: 34px; height: 34px; background: var(--navy); }
  .brand-name { font-size: 56px; font-weight: 700; color: var(--navy); letter-spacing: 0.5px; line-height: 1; }

  .holder { position: absolute; left: 54px; top: 268px; font-size: 27px; color: var(--navy); }
  .holder-name { font-weight: 700; }
  .holder-role { font-weight: 400; font-size: 23px; color: var(--ink-soft); }

  .band { position: absolute; left: 0; top: 326px; width: 100%; height: 190px; background: var(--navy); }

  .accent-disc {
    position: absolute; left: 620px; top: 226px; width: 190px; height: 178px;
    border-radius: 50%; background: var(--mist); border: 8px solid var(--white);
  }

  .contacts { position: absolute; left: 60px; top: 364px; list-style: none; }
  .contacts li {
    display: flex; align-items: center; gap: 12px;
    height: 32px; font-size: 20px; color: var(--white);
  }
  .contacts svg { width: 17px; height: 17px; flex: none; }

  .divider { position: absolute; left: 470px; top: 430px; width: 1px; height: 60px; background: rgba(255,255,255,0.55); }
  .address { position: absolute; left: 492px; top: 428px; font-size: 22px; line-height: 32px; color: var(--white); font-style: normal; }

  /* Back */
  .card-back { left: 49px; top: 606px; background: var(--navy); }
  .back-brand {
    position: absolute; left: 0; top: 170px; width: 100%;
    display: flex; justify-content: center; align-items: center; gap: 20px;
  }
  .back-brand .brand-mark { background: var(--white); width: 40px; height: 40px; }
  .back-brand .brand-name { color: var(--white); font-size: 64px; }
  .back-url {
    position: absolute; left: 0; top: 372px; width: 100%; text-align: center;
    font-size: 29px; letter-spacing: 2.5px; color: var(--white);
  }
</style>
</head>
<body>
<main class="canvas">

  <section class="card card-front">
    <div class="brand">
      <span class="brand-mark"></span>
      <span class="brand-name">Riverpeak Analytics</span>
    </div>

    <p class="holder"><span class="holder-name">Marcus Helvard,</span> <span class="holder-role">Managing Director</span></p>

    <div class="band"></div>
    <div class="accent-disc"></div>

    <ul class="contacts">
      <li>
        <svg viewBox="0 0 20 20" fill="none" stroke="#fff" stroke-width="1.8"><circle cx="10" cy="10" r="8.5"/><path d="M7 5.5c-1 1 -.5 3.5 1.5 5.5s4.5 2.5 5.5 1.5l-1.5-1.5-1.5 1c-1-.5-2.5-2-3-3l1-1.5z" fill="#fff" stroke="none"/></svg>
        1300 582 417
      </li>
      <li>
        <svg viewBox="0 0 20 20" fill="none" stroke="#fff" stroke-width="1.8"><rect x="5.5" y="1.5" width="9" height="17" rx="1.5"/><rect x="7.5" y="4" width="5" height="5" fill="#fff" stroke="none"/></svg>
        0450 731 258
      </li>
      <li>
        <svg viewBox="0 0 20 20" fill="none" stroke="#fff" stroke-width="1.8"><rect x="2" y="5" width="16" height="11" rx="1"/><path d="M2 6l8 6 8-6"/></svg>
        marcus@riverpeakanalytics.example.au
      </li>
      <li>
        <svg viewBox="0 0 20 20" fill="none" stroke="#fff" stroke-width="1.5"><circle cx="10" cy="10" r="8.5"/><ellipse cx="10" cy="10" rx="3.8" ry="8.5"/><path d="M1.5 10h17M3 5.5h14M3 14.5h14"/></svg>
        www.riverpeakanalytics.example.au
      </li>
    </ul>

    <div class="divider"></div>
    <address class="address">27/15 Marlowe Street<br>Fernbrook NSW 2199</address>
  </section>

  <section class="card card-back">
    <div class="back-brand">
      <span class="brand-mark"></span>
      <span class="brand-name">Riverpeak Analytics</span>
    </div>
    <p class="back-url">www.riverpeakanalytics.example.au</p>
  </section>

</main>
</body>
</html>
```